2016 Calendar

12 months illustration around a provided grid (template attached) for a 2016 Family Organiser. I would like a concept developed and 2 month samples of that concept submitted for consideration. I would want the project completed in a 1 month time frame. They need to be done in InDesign. So my graphic artist can extract illustration etc to do the front and back covers and import holidays. The 2014 calendar designs can be seen at our webpage www.brightplanners7.com.au and I have attached files of our 3 x 2015 designs to give you a broader idea of what we do currently. Friendly, feel good illustrations that families can relate to and I love humour, so if the illustration makes one smile or laugh, even better, but not necessary. I normally include a quote, but are happy to look at other ideas that might appeal, if you have some fun facts etc. If the graphic artist isn't able to come up with quotes I am happy to find these to compliment the illustration, but space must be left for a quote to go in.

```html
<!DOCTYPE html>
<html lang="en">
<head>
<meta charset="utf-8">
<title>September Family Organiser</title>
<link href="https://fonts.googleapis.com/css2?family=Arimo:wght@400;700&family=Chewy&family=Patrick+Hand&display=swap" rel="stylesheet">
<style>
  :root{
    --roof:#f2b6a8;
    --roof-edge:#d98c7c;
    --wall-top:#e9e9e7;
    --wall-bottom:#dcdcda;
    --paving-light:#cfcfcd;
    --paving-dark:#9d9d9b;
    --sign-wood:#b98a52;
    --sign-face:#f6f1e2;
    --month-ink:#1f4e7a;
    --post-wood:#b58753;
    --post-ink:#ffffff;
    --scene-green:#7fbf3f;
    --scene-blue:#3f7fc0;
    --scene-brick:#b8aa98;
    --flower:#e8415e;
    --grid-line:#9a9a9a;
    --cell:#ffffff;
    --sunday:#fdf0e0;
    --brown:#9a4d16;
    --ink:#1a1a1a;
    --note:#8a8a8a;
  }
  *{box-sizing:border-box;margin:0;padding:0}
  html,body{width:826px;height:1200px;overflow:hidden;background:#fff}
  .page{
    position:relative;width:826px;height:1200px;overflow:hidden;
    background:linear-gradient(180deg,var(--wall-top) 0,var(--wall-bottom) 283px,var(--paving-light) 285px,var(--paving-dark) 1200px);
    font-family:"Arimo",Arial,sans-serif;color:var(--ink);
  }
  .roof{position:absolute;left:0;top:0;width:826px;height:34px}
  .month-sign{position:absolute;left:64px;top:38px;width:324px;height:214px}
  .month-name{
    position:absolute;left:64px;top:95px;width:324px;text-align:center;
    font-family:"Chewy","Patrick Hand",cursive;font-size:66px;color:var(--month-ink);letter-spacing:1px;
  }
  .garden-scene{position:absolute;left:406px;top:70px;width:420px;height:264px}
  .flower-bunch{position:absolute;left:42px;top:268px;width:92px;height:66px}
  .quote-post{position:absolute;left:638px;top:80px;width:128px;height:112px;transform:rotate(4deg)}
  .quote{
    position:absolute;left:642px;top:94px;width:122px;transform:rotate(4deg);
    font-family:"Patrick Hand",cursive;color:var(--post-ink);text-align:center;font-size:14px;line-height:23px;
  }
  .quote-author{display:block;text-align:right;font-family:"Arimo",sans-serif;font-size:7px;color:#333;line-height:12px;margin-top:2px}

  .planner{position:absolute;left:27px;border-collapse:collapse;table-layout:fixed;width:771px}
  .planner td{border:1px solid var(--grid-line);background:var(--cell);height:24.5px;padding:0;vertical-align:middle;position:relative}
  .planner .day{font-weight:700;font-size:13px;padding-left:5px;white-space:nowrap}
  .planner .day b{display:inline-block;width:48px;font-weight:700}
  .planner .num{text-align:center;font-size:13px;font-weight:400}
  .planner tr.sunday td{background:var(--sunday);color:var(--brown)}
  .names{top:334px}
  .names td{height:22px;background:rgba(255,255,255,.85)}
  .names .label{color:var(--brown);font-weight:700;font-size:14px;padding-left:6px}
  .block-one{top:370px}
  .block-two{top:615px}
  .note{position:absolute;font-size:7px;color:var(--note);white-space:nowrap}
  .note.left{left:5px;top:8px}
  .note.right{right:6px;top:14px}
  .moon{position:absolute;left:8px;top:6px;width:11px;height:11px}

  .moon-key{position:absolute;top:1172px;width:11px;height:11px}
  .site{position:absolute;right:4px;top:1173px;font-size:8px;color:#fff}
</style>
</head>
<body>
<div class="page">
  <svg class="roof" viewBox="0 0 826 34" role="img" aria-label="Pink roof tile edge">
    <rect width="826" height="34" fill="var(--roof)"/>
    <rect y="28" width="826" height="6" fill="var(--roof-edge)"/>
  </svg>

  <svg class="month-sign" viewBox="0 0 324 214" role="img" aria-label="Hanging wooden sign with leaves">
    <rect x="0" y="20" width="324" height="194" rx="70" fill="var(--sign-wood)"/>
    <rect x="18" y="36" width="288" height="162" rx="60" fill="var(--sign-face)"/>
  </svg>
  <div class="month-name">September</div>

  <div class="garden-scene" role="img" aria-label="Garden scene with a brick patch, flower crate on a blue stool, plants and a white picket fence"
       style="background:linear-gradient(160deg,rgba(184,170,152,.55) 0,rgba(184,170,152,.2) 35%,rgba(127,191,63,.35) 60%,rgba(63,127,192,.35) 100%)"></div>
  <div class="flower-bunch" role="img" aria-label="Bunch of colourful flowers"
       style="background:radial-gradient(circle,var(--flower) 0,#f48aa0 55%,rgba(127,191,63,.6) 100%);border-radius:50% 50% 10% 10%"></div>

  <div class="quote-post" role="img" aria-label="Wooden signpost" style="background:var(--post-wood);border-radius:4px"></div>
  <p class="quote">With the coming<br>of spring<br>I am calm again!<span class="quote-author">Anton Reiler</span></p>

  <table class="planner names">
    <colgroup><col style="width:67px"><col style="width:113px"><col style="width:111px"><col style="width:112px"><col style="width:112px"><col style="width:112px"><col style="width:112px"><col style="width:32px"></colgroup>
    <tr><td class="label" colspan="2">NAMES</td><td></td><td></td><td></td><td></td><td></td><td></td></tr>
  </table>

  <table class="planner block-one">
    <colgroup><col style="width:67px"><col style="width:113px"><col style="width:111px"><col style="width:112px"><col style="width:112px"><col style="width:112px"><col style="width:112px"><col style="width:32px"></colgroup>
    <tr><td class="day"><b>THUR</b>1</td><td><span class="note left">New Year's Day</span></td><td></td><td></td><td></td><td></td><td></td><td class="num">1</td></tr>
    <tr><td class="day"><b>FRI</b>2</td><td></td><td></td><td></td><td></td><td></td><td><span class="note right">Day After New Year's Day (NZ)</span></td><td class="num">2</td></tr>
    <tr><td class="day"><b>SAT</b>3</td><td></td><td></td><td></td><td></td><td></td><td></td><td class="num">3</td></tr>
    <tr class="sunday"><td class="day"><b>SUN</b>4</td><td></td><td></td><td></td><td></td><td></td><td></td><td class="num">4</td></tr>
    <tr><td class="day"><b>MON</b>5</td><td><svg class="moon" viewBox="0 0 12 12"><circle cx="6" cy="6" r="5" fill="#fff" stroke="#000"/></svg></td><td></td><td></td><td></td><td></td><td></td><td class="num">5</td></tr>
    <tr><td class="day"><b>TUE</b>6</td><td></td><td></td><td></td><td></td><td></td><td></td><td class="num">6</td></tr>
    <tr><td class="day"><b>WED</b>7</td><td></td><td></td><td></td><td></td><td></td><td></td><td class="num">7</td></tr>
    <tr><td class="day"><b>THUR</b>8</td><td></td><td></td><td></td><td></td><td></td><td></td><td class="num">8</td></tr>
    <tr><td class="day"><b>FRI</b>9</td><td></td><td></td><td></td><td></td><td></td><td></td><td class="num">9</td></tr>
  </table>

  <table class="planner block-two">
    <colgroup><col style="width:67px"><col style="width:113px"><col style="width:111px"><col style="width:112px"><col style="width:112px"><col style="width:112px"><col style="width:112px"><col style="width:32px"></colgroup>
    <tr><td class="day"><b>SAT</b>10</td><td></td><td></td><td></td><td></td><td></td><td></td><td class="num">10</td></tr>
    <tr class="sunday"><td class="day"><b>SUN</b>11</td><td></td><td></td><td></td><td></td><td></td><td></td><td class="num">11</td></tr>
    <tr><td class="day"><b>MON</b>12</td><td></td><td></td><td></td><td></td><td></td><td></td><td class="num">12</td></tr>
    <tr><td class="day"><b>TUE</b>13</td><td><svg class="moon" viewBox="0 0 12 12"><circle cx="6" cy="6" r="5" fill="#fff" stroke="#000"/><path d="M6 1a5 5 0 0 0 0 10z"/></svg></td><td></td><td></td><td></td><td></td><td></td><td class="num">13</td></tr>
    <tr><td class="day"><b>WED</b>14</td><td></td><td></td><td></td><td></td><td></td><td></td><td class="num">14</td></tr>
    <tr><td class="day"><b>THUR</b>15</td><td></td><td></td><td></td><td></td><td></td><td></td><td class="num">15</td></tr>
    <tr><td class="day"><b>FRI</b>16</td><td></td><td></td><td></td><td></td><td></td><td></td><td class="num">16</td></tr>
    <tr><td class="day"><b>SAT</b>17</td><td></td><td></td><td></td><td></td><td></td><td></td><td class="num">17</td></tr>
    <tr class="sunday"><td class="day"><b>SUN</b>18</td><td></td><td></td><td></td><td></td><td></td><td></td><td class="num">18</td></tr>
    <tr><td class="day"><b>MON</b>19</td><td></td><td></td><td></td><td></td><td></td><td></td><td class="num">19</td></tr>
    <tr><td class="day"><b>TUE</b>20</td><td><svg class="moon" viewBox="0 0 12 12"><circle cx="6" cy="6" r="5.5"/></svg></td><td></td><td></td><td></td><td></td><td></td><td class="num">20</td></tr>
    <tr><td class="day"><b>WED</b>21</td><td></td><td></td><td></td><td></td><td></td><td></td><td class="num">21</td></tr>
    <tr><td class="day"><b>THUR</b>22</td><td></td><td></td><td></td><td></td><td></td><td></td><td class="num">22</td></tr>
    <tr><td class="day"><b>FRI</b>23</td><td></td><td></td><td></td><td></td><td></td><td></td><td class="num">23</td></tr>
    <tr><td class="day"><b>SAT</b>24</td><td></td><td></td><td></td><td></td><td></td><td></td><td class="num">24</td></tr>
    <tr class="sunday"><td class="day"><b>SUN</b>25</td><td></td><td></td><td></td><td></td><td></td><td></td><td class="num">25</td></tr>
    <tr><td class="day"><b>MON</b>26</td><td></td><td></td><td></td><td></td><td></td><td><span class="note right" style="right:22px">Australia Day</span></td><td class="num">26</td></tr>
    <tr><td class="day"><b>TUE</b>27</td><td><svg class="moon" viewBox="0 0 12 12"><circle cx="6" cy="6" r="5" fill="#fff" stroke="#000"/><path d="M6 1a5 5 0 0 1 0 10z"/></svg></td><td></td><td></td><td></td><td></td><td></td><td class="num">27</td></tr>
    <tr><td class="day"><b>WED</b>28</td><td></td><td></td><td></td><td></td><td></td><td></td><td class="num">28</td></tr>
    <tr><td class="day"><b>THUR</b>29</td><td></td><td></td><td></td><td></td><td></td><td></td><td class="num">29</td></tr>
    <tr><td class="day"><b>FRI</b>30</td><td></td><td></td><td></td><td></td><td></td><td></td><td class="num">30</td></tr>
    <tr><td class="day"><b>SAT</b>31</td><td></td><td></td><td></td><td></td><td></td><td></td><td class="num">31</td></tr>
  </table>

  <svg class="moon-key" style="left:27px" viewBox="0 0 12 12"><circle cx="6" cy="6" r="5" fill="#fff" stroke="#000"/></svg>
  <svg class="moon-key" style="left:90px" viewBox="0 0 12 12"><circle cx="6" cy="6" r="5" fill="#fff" stroke="#000"/><path d="M6 1a5 5 0 0 0 0 10z"/></svg>
  <svg class="moon-key" style="left:165px" viewBox="0 0 12 12"><circle cx="6" cy="6" r="5.5"/></svg>
  <svg class="moon-key" style="left:230px" viewBox="0 0 12 12"><circle cx="6" cy="6" r="5" fill="#fff" stroke="#000"/><path d="M6 1a5 5 0 0 1 0 10z"/></svg>
  <span class="site">www.brightplanners7.com.au</span>
</div>
</body>
</html>
```